Middle Eastern Wordpress Design for Velmora Initiative's Museum

We need a new website design for Velmora, “Our Homes” in Judeo-Arabic,” a project that explores the unfolding of Jewish history through the prism of physical location by digitizing individual sites (schools, cemeteries, synagogues, shrines) and memories.
The website should have the look and feel of a museum, as it will serve as the Velmora Initiative's Terra-Gallery of Levantine Heritage Life.
Velmora pioneers the use of digital mapping and other technologies to weave and synthesize satellite imagery (complete with terrain, zoomable perspectives, tiltable views, and 360-degree rotation), immersive panoramas, three-dimensional architectural models, archival and contemporary photography, and oral history recordings. In this way and no other, the project ensures untrammeled access to often endangered Jewish historic and cultural sites, allowing anyone with an Internet connection to travel across the region as if on eagles’ wings, unaffected by political and interreligious strife below. Previously unknown or difficult to visit sites are now “visitable” through Velmora.
Driven by a team with diverse backgrounds and outlooks—including young Muslims eager to discover shared history—Velmora:
• Uncovers all manner of historic sites, famous and obscure, throughout the region;
• Preserves sites and memories via maps and multimedia; and
• Perpetuates what would otherwise be lost or forgotten by transforming research materials into exhibitions, educational applications, and a database-driven cultural atlas.
Velmora's website design needs to be clean and informational and exciting as well as showcase the best of our collection.
The template should have a distinctive homepage, themed pages (about, news, screening rooms to view multimedia content, exhibit wings and tours, opportunities), and no blog elements (e.g., comment section). Admin friendliness is a plus.
A separate design contest for Velmora's new logo is posted here: http://tasks.craftplume-example.com/task.aspx?id=48170

```html
<!DOCTYPE html>
<html lang="en">
<head>
<meta charset="utf-8">
<title>Velmora — Terra-Gallery of Levantine Heritage Life</title>
<link href="https://fonts.googleapis.com/css2?family=Alegreya:wght@400;700&family=Marcellus&family=Open+Sans:wght@400;700&display=swap" rel="stylesheet">
<style>
:root{
  --header-top:#6e6e6e;
  --header-bottom:#3a3a3a;
  --nav-bg:#f1f1f1;
  --nav-text:#2a2a2a;
  --home-tab:#cbbb93;
  --dropdown:#6a6a6a;
  --dropdown-active:#7a1414;
  --stage:#9a9a9a;
  --stage-band:#8a8a8a;
  --panel:#d3d3d5;
  --title:#7a5a1e;
  --subtitle:#84652a;
  --body:#2d2d2d;
  --footer:#8f8f8f;
  --frame:#ffffff;
}
*{box-sizing:border-box;margin:0;padding:0}
html,body{width:820px;height:1200px;overflow:hidden}
body{background:var(--stage);font-family:'Alegreya',serif;color:var(--body);position:relative}
.site-header{height:88px;background:linear-gradient(var(--header-top),var(--header-bottom));text-align:center;padding-top:20px;color:#fff}
.brand{display:inline-flex;align-items:center;gap:8px;font-family:'Marcellus',serif;font-size:32px;letter-spacing:1px}
.brand-dot{width:16px;height:16px;border:2px solid #fff;border-radius:50%}
.tagline{font-family:'Open Sans',sans-serif;font-weight:700;font-size:7.5px;letter-spacing:.4px;margin-top:4px}
.main-nav{height:34px;background:var(--nav-bg);display:flex;align-items:center;position:relative;border-bottom:1px solid #bbb}
.main-nav a{font-family:'Marcellus',serif;font-size:15.5px;color:var(--nav-text);text-decoration:none;position:absolute;top:6px}
.main-nav .home{left:8px;top:1px;width:78px;height:32px;background:var(--home-tab);text-align:center;line-height:30px}
.dropdown{position:absolute;left:91px;top:122px;width:119px;height:84px;background:var(--dropdown);padding-top:14px;z-index:3}
.dropdown::before{content:"";position:absolute;left:36px;top:0;border:6px solid transparent;border-top-color:var(--nav-bg)}
.dropdown li{list-style:none;font-family:'Open Sans',sans-serif;font-size:11.5px;color:#fff;height:20px;line-height:17px;padding-left:25px}
.dropdown li.active{background:var(--dropdown-active);margin-right:0;position:relative}
.dropdown li.active::before{content:"";position:absolute;left:12px;top:5px;border:4px solid transparent;border-left:5px solid #fff}
.stage{position:absolute;top:122px;left:0;width:820px;height:333px;background:linear-gradient(#a3a3a3,#8e8e8e)}
.stage-band{position:absolute;left:0;top:134px;width:820px;height:76px;background:rgba(60,60,60,.25)}
.slide{position:absolute;border:4px solid var(--frame);border-radius:8px;box-shadow:0 3px 8px rgba(0,0,0,.4)}
.slide-left{left:64px;top:108px;width:150px;height:126px;background:linear-gradient(135deg,#b37a45,#5a3a22)}
.slide-right{left:606px;top:108px;width:142px;height:126px;background:linear-gradient(135deg,#8a7a5a,#3c3c4a)}
.slide-main{left:206px;top:28px;width:410px;height:276px;background:linear-gradient(#c9c9c9 0%,#dcdcd8 30%,#8aa6c2 55%,#3f7fb8 75%,#7a6d5a 100%);z-index:2}
.arrow{position:absolute;top:157px;width:28px;height:28px}
.content{position:absolute;left:10px;top:455px;width:800px;height:682px;background:var(--panel);padding:10px 20px 0 22px}
.content h1{font-family:'Alegreya',serif;font-weight:400;font-size:25px;color:var(--title);margin-bottom:14px}
.intro{font-size:11.5px;line-height:19.5px;text-align:justify}
.content h2{font-family:'Alegreya',serif;font-weight:700;font-size:13.5px;line-height:19px;color:var(--subtitle);margin:18px 80px 6px 6px}
.points{width:416px;margin-left:6px;font-size:11.5px;line-height:19.5px;text-align:justify;list-style:none}
.more{position:absolute;left:435px;top:314px;width:62px;height:16px;border-radius:8px;background:linear-gradient(#a59c86,#5e574a);color:#2a2210;font-weight:700;font-size:11px;text-align:center;line-height:15px}
.video{position:absolute;left:210px;top:348px;width:380px;height:232px;background:#222}
.video-screen{position:absolute;left:0;top:0;width:380px;height:206px;background:linear-gradient(135deg,#3a3a3a,#9a9a9a 50%,#2a2a2a)}
.video-tabs{position:absolute;left:6px;top:3px;font-family:'Open Sans',sans-serif;font-size:8px;color:#fff;background:#111;padding:1px 4px;letter-spacing:.3px}
.credit{position:absolute;right:6px;top:10px;font-family:'Open Sans',sans-serif;font-size:6.5px;color:#fff;text-align:right;font-weight:700}
.video-bar{position:absolute;left:0;top:206px;width:380px;height:26px;background:linear-gradient(#e8e8e8,#bdbdbd)}
.outro{position:absolute;left:28px;top:590px;width:752px;font-size:11.5px;line-height:19.5px;text-align:justify}
.site-footer{position:absolute;top:1137px;left:0;width:820px;height:63px;background:var(--footer)}
.copyright{position:absolute;left:0;width:820px;top:20px;text-align:center;font-size:11px}
.social{position:absolute;top:8px;width:30px;height:30px;border-radius:50%;background:radial-gradient(#e5e5e5,#8a8a8a);border:1px solid #666}
</style>
</head>
<body>
<header class="site-header">
  <div class="brand"><span class="brand-dot"></span>Velmora</div>
  <div class="tagline">TERRA-GALLERY OF LEVANTINE HERITAGE LIFE</div>
</header>
<nav class="main-nav">
  <a class="home" href="#">Home</a>
  <a href="#" style="left:117px">About</a>
  <a href="#" style="left:195px">Collection</a>
  <a href="#" style="left:294px">Education</a>
  <a href="#" style="left:390px">Special Exhibits</a>
  <a href="#" style="left:516px">News</a>
  <a href="#" style="left:574px">Support</a>
  <a href="#" style="left:660px">Gift shop</a>
  <a href="#" style="left:756px">Contact</a>
</nav>
<section class="stage">
  <div class="stage-band"></div>
  <div class="slide slide-left" role="img" aria-label="Interior of a historic synagogue hall with chandeliers"></div>
  <div class="slide slide-right" role="img" aria-label="Synagogue interior with a menorah and blue curtains"></div>
  <div class="slide slide-main" role="img" aria-label="Tiled courtyard of a whitewashed heritage building with blue benches"></div>
  <svg class="arrow" style="left:30px" viewBox="0 0 28 28"><circle cx="14" cy="14" r="12" fill="#eee" stroke="#555" stroke-width="2"/><path d="M17 8 L10 14 L17 20" fill="none" stroke="#333" stroke-width="3"/></svg>
  <svg class="arrow" style="left:755px" viewBox="0 0 28 28"><circle cx="14" cy="14" r="12" fill="#eee" stroke="#555" stroke-width="2"/><path d="M11 8 L18 14 L11 20" fill="none" stroke="#333" stroke-width="3"/></svg>
</section>
<ul class="dropdown">
  <li class="active">Approbations</li>
  <li>Partners</li>
  <li>People</li>
</ul>
<main class="content">
  <h1>Welcome To Velmora</h1>
  <p class="intro">Velmora pioneers the use of digital mapping and other technologies to weave and synthesize satellite imagery (complete with terrain, zoomable perspectives, tiltable views, and 360-degree rotation), immersive panoramas, three-dimensional architectural models, archival and contemporary photography, and oral history recordings. In this way and no other, the project ensures untrammeled access to often endangered Jewish historic and cultural sites, allowing anyone with an Internet connection to travel across the region as if on eagles' wings, unaffected by political and interreligious strife below. Previously unknown or difficult to visit sites are now "visitable" through Velmora.</p>
  <h2>Driven by a team with diverse backgrounds and outlooks—including young Muslims eager to discover shared history—Velmora:</h2>
  <ul class="points">
    <li>• Uncovers all manner of historic sites, famous and obscure, throughout the region;</li>
    <li>• Preserves sites and memories via maps and multimedia; and</li>
    <li>• Perpetuates what would otherwise be lost or forgotten by transforming research materials into exhibitions, educational applications, and a database-driven cultural atlas.</li>
  </ul>
  <div class="more">more...</div>
  <div class="video">
    <div class="video-screen" role="img" aria-label="Panorama of a three-dimensional architectural model with staircases"></div>
    <div class="video-tabs">FULLSCREEN &nbsp; EMBED &amp; SHARE</div>
    <div class="credit">Panorama by<br>Lena Vask</div>
    <svg style="position:absolute;left:292px;top:150px" width="22" height="58" viewBox="0 0 22 58"><rect x="1" y="1" width="20" height="56" rx="3" fill="#ddd" stroke="#888"/><rect x="8" y="18" width="6" height="34" fill="#e0561a"/><rect x="5" y="14" width="12" height="6" fill="#fff" stroke="#777"/></svg>
    <div class="video-bar">
      <svg width="380" height="26" viewBox="0 0 380 26">
        <rect x="6" y="4" width="24" height="17" rx="2" fill="#ddd" stroke="#888"/><path d="M15 8 L22 12.5 L15 17Z" fill="#333"/>
        <rect x="46" y="9" width="180" height="8" rx="4" fill="#777"/><rect x="46" y="9" width="42" height="8" rx="4" fill="#e0561a"/><circle cx="88" cy="13" r="5" fill="#eee" stroke="#777"/>
        <text x="232" y="16" font-family="Open Sans, sans-serif" font-size="7" fill="#333">1:47 / 12:35</text>
        <rect x="292" y="4" width="22" height="17" rx="2" fill="#ddd" stroke="#888"/><path d="M297 10 h3 l4 -3 v11 l-4 -3 h-3z" fill="#333"/>
        <rect x="320" y="4" width="22" height="17" rx="2" fill="#ddd" stroke="#888"/><text x="324" y="16" font-family="Open Sans, sans-serif" font-size="8" font-weight="700" fill="#333">HD</text>
        <rect x="348" y="4" width="22" height="17" rx="2" fill="#ddd" stroke="#888"/><path d="M353 8 h4 M353 8 v4 M365 8 h-4 M365 8 v4 M353 18 h4 M353 18 v-4 M365 18 h-4 M365 18 v-4" stroke="#333" stroke-width="1.5"/>
      </svg>
    </div>
  </div>
  <p class="outro">Lorem Ipsum is simply dummy text of the printing and typesetting industry. Lorem Ipsum has been the industry's standard dummy text ever since the 1500s, when an unknown printer took a galley of type and scrambled it to make a type specimen book. It has survived not only five centuries, but also the leap into electronic typesetting,</p>
</main>
<footer class="site-footer">
  <p class="copyright">Copyright (c) 2011. www.velmora-example.org</p>
  <span class="social" style="left:700px"></span>
  <span class="social" style="left:735px"></span>
  <span class="social" style="left:770px"></span>
</footer>
</body>
</html>
```